BrightLoop Kiosk Business Card Design Project

BrightLoop Kiosk requires a business card design. We hire PhotoBooths to events such as Birthday Parties, Hens and Bucks Night, Anniversaries, Corporate Functions
, Engagements, Theme Nights, Presentation Night etc.
Business Card needs to look Modern, Professional And Catchy.
Updates

Hello Thankyou for all of your great designs, contact information will be provided shortly. We are considering the front of the card to be white themed and the back of the card to be black themed. And all social media colours to be their original colour. Thankyou

Hello everyone, Here are the contact details: Martin Colby - Manager Mobile number - 0491738205 Website - www.brightloopkiosk.example Email - admin@brightloopkiosk.example And if you can add the word "weddings" in the "We cater For" section would be good. Thankyou

Target Market(s)

Birthday Parties
Hens and Bucks Night
Weddings
Corporate Functions
Engagements
Theme Nights
Presentation Night
School Functions

Industry/Entity Type

Events

Requirements
Must have
• Must Match Logo
Must Have www.brightloopkiosk.example

On Back of card must have social media icons Facebook, Twitter, Youtube, Linkin and

We Cater For:

Birthday Parties
Hens and Bucks Night
Anniversaries
Corporate Functions
Engagements
Theme Nights
Presentation Night
School Functions
And more.....

```html
<!DOCTYPE html>
<html lang="en">
<head>
<meta charset="utf-8">
<title>BrightLoop Kiosk – Business Cards</title>
<link href="https://fonts.googleapis.com/css2?family=Josefin+Sans:wght@400;600&family=Cinzel:wght@500&display=swap" rel="stylesheet">
<style>
  :root {
    --page: #e6e7e9;
    --card: #f6f6f6;
    --ink: #1c1c1c;
    --muted: #555a5e;
    --accent: #1aa7d3;
    --band-dark: #0b0b0b;
    --social-1: #3b5998;
    --social-2: #55acee;
    --social-3: #0e76a8;
    --social-4: #e62117;
  }
  * { box-sizing: border-box; margin: 0; padding: 0; }
  html, body { width: 1200px; height: 900px; overflow: hidden; }
  body {
    background: var(--page);
    font-family: "Josefin Sans", "Century Gothic", sans-serif;
    color: var(--ink);
    position: relative;
  }
  .card {
    position: absolute;
    width: 588px;
    height: 336px;
    background: var(--card);
    box-shadow: 0 6px 18px rgba(0,0,0,.12);
    overflow: hidden;
  }
  .card--back { left: 306px; top: 70px; }
  .card--front { left: 306px; top: 484px; }

  .brand { display: flex; align-items: center; gap: 12px; }
  .brand__mark { width: 26px; height: 26px; background: var(--accent); flex: none; }
  .brand__name {
    font-weight: 600;
    font-size: 28px;
    letter-spacing: 1px;
    text-transform: uppercase;
    color: var(--ink);
    line-height: 1;
  }

  /* back */
  .card--back .brand { position: absolute; left: 0; right: 0; top: 34px; justify-content: center; }
  .services {
    position: absolute; left: 0; right: 0; top: 82px;
    text-align: center;
    font-size: 10px;
    letter-spacing: 1.4px;
    text-transform: uppercase;
    color: var(--muted);
    line-height: 22px;
    white-space: nowrap;
  }
  .services__sep { margin: 0 7px; }
  .social {
    position: absolute; left: 0; right: 0; top: 186px;
    display: flex; justify-content: center; gap: 10px;
  }
  .social__tile { width: 28px; height: 28px; border-radius: 2px; }
  .social__tile--1 { background: var(--social-1); }
  .social__tile--2 { background: var(--social-2); }
  .social__tile--3 { background: var(--social-3); }
  .social__tile--4 { background: var(--social-4); }
  .band-accent {
    position: absolute; left: 0; right: 0; top: 238px;
    height: 30px; background: var(--accent);
  }

  /* front */
  .card--front .brand { position: absolute; left: 40px; top: 40px; }
  .band-dark {
    position: absolute; left: 0; right: 0; bottom: 14px;
    height: 44px; background: var(--band-dark);
  }
  .band-dark__mark {
    position: absolute; left: 178px; top: 8px;
    width: 28px; height: 28px; background: var(--card);
    border: 6px solid var(--accent);
  }
  .contact { position: absolute; left: 300px; top: 92px; }
  .contact__name {
    font-family: "Cinzel", serif;
    font-weight: 500;
    font-size: 20px; letter-spacing: 4px; color: var(--ink);
    line-height: 24px;
  }
  .contact__role {
    font-size: 11px; letter-spacing: 2px; color: var(--muted);
    line-height: 14px; margin: 2px 0 10px;
  }
  .contact__line {
    display: flex; align-items: center; gap: 10px;
    font-size: 12px; letter-spacing: 1.4px; color: var(--ink);
    line-height: 14px; margin-bottom: 4px;
  }
  .contact__line svg { width: 12px; height: 12px; fill: var(--accent); flex: none; }
  .contact__address {
    font-size: 11px; letter-spacing: 1.8px; text-transform: uppercase;
    color: var(--ink); line-height: 16px; margin-top: 6px;
  }
</style>
</head>
<body>

<section class="card card--back" aria-label="Back of card">
  <div class="brand">
    <span class="brand__mark"></span>
    <span class="brand__name">BrightLoop Kiosk</span>
  </div>
  <p class="services">
    Birthday Parties<span class="services__sep">•</span>Hens and Bucks Night<span class="services__sep">•</span>Anniversaries<br>
    Corporate Functions<span class="services__sep">•</span>Engagements<span class="services__sep">•</span>Theme Nights<span class="services__sep">•</span>Weddings<br>
    Presentation Night<span class="services__sep">•</span>School Functions<br>
    And More.....
  </p>
  <div class="social" aria-label="Social media">
    <span class="social__tile social__tile--1"></span>
    <span class="social__tile social__tile--2"></span>
    <span class="social__tile social__tile--3"></span>
    <span class="social__tile social__tile--4"></span>
  </div>
  <div class="band-accent"></div>
</section>

<section class="card card--front" aria-label="Front of card">
  <div class="brand">
    <span class="brand__mark"></span>
    <span class="brand__name">BrightLoop Kiosk</span>
  </div>

  <div class="contact">
    <h1 class="contact__name">MARTIN COLBY</h1>
    <p class="contact__role">CEO</p>
    <p class="contact__line">
      <svg viewBox="0 0 12 12"><path d="M2.5 0.5 L4.5 0.5 L5.2 3.2 L3.8 4.2 C4.5 5.8 6.2 7.5 7.8 8.2 L8.8 6.8 L11.5 7.5 L11.5 9.5 C11.5 10.8 10.6 11.5 9.5 11.5 C4.5 11 1 7.5 0.5 2.5 C0.5 1.4 1.2 0.5 2.5 0.5 Z"/></svg>
      0491 738 205
    </p>
    <p class="contact__line">
      <svg viewBox="0 0 12 12"><path d="M3 0 H9 A1 1 0 0 1 10 1 V11 A1 1 0 0 1 9 12 H3 A1 1 0 0 1 2 11 V1 A1 1 0 0 1 3 0 Z M3.2 1.5 V9.5 H8.8 V1.5 Z M5.4 10.2 H6.6 V11.2 H5.4 Z"/></svg>
      0491 738 206
    </p>
    <p class="contact__line">
      <svg viewBox="0 0 12 12"><path d="M0 2 H12 V10 H0 Z M1 3 L6 6.8 L11 3 V2.9 H1 Z"/></svg>
      admin@brightloopkiosk.example
    </p>
    <p class="contact__line">
      <svg viewBox="0 0 12 12"><path d="M6 0 A6 6 0 1 0 6 12 A6 6 0 1 0 6 0 Z M6 1.2 A4.8 4.8 0 1 1 6 10.8 A4.8 4.8 0 1 1 6 1.2 Z M1.5 5.4 H10.5 V6.6 H1.5 Z M5.4 1 H6.6 V11 H5.4 Z"/></svg>
      www.brightloopkiosk.example
    </p>
    <p class="contact__address">12 Harbour Lane<br>Suite 4 Lakeview<br>NS 2040</p>
  </div>

  <div class="band-dark"><span class="band-dark__mark"></span></div>
</section>

</body>
</html>
```